We are Here! Come and Meet the Team Flyer

A clear and quirky, flyer to let local Residents know we have landed.
Based around our logo.

We avoid anything medical but rather focus on being pet-centred, warmth, approachable and community-orientated.

We pride ourselves on being cutting-edge but steer away from a cold sterile image.
Approachability, uptodate. We understandt hat pets are part of a family and we will provide the level of care that we would expect for our own pets.

Target Market(s)

Residents in the area

Industry/Entity Type

Veterinary

Font styles to use
Sans Serif

Colors
33b8a4
ffc214
0255a3

Requirements
Must have
• Logo and PERHAPS a location of Clinic indicated on the cat of the Logo.
• NOW OPEN!
• 1) Exact location of the Clinic indicated: the lefthand side of tail, near the cat's back.
• 2) Warm, quirky, Approachable
• 3) Contact details (see attached draft Poster)
• 4) Location: Silver Brook Arcade, Building 4, Mezzanine level
Should not have
• nothing medical or cliched.

```html
<!DOCTYPE html>
<html lang="en">
<head>
<meta charset="utf-8">
<title>Kindred Paws – Now Open Flyer</title>
<link href="https://fonts.googleapis.com/css2?family=Saira:wght@500;600;700&family=Carlito:wght@400;700&display=swap" rel="stylesheet">
<style>
  :root {
    --sage: #8dbda0;
    --sage-dark: #7aae90;
    --charcoal: #2c2c2c;
    --ink: #262626;
    --orange: #f0921a;
    --orange-deep: #e9841a;
    --sky: #27aee0;
    --paper: #f3f3f3;
    --white: #ffffff;
    --stage: #3a3a3a;
  }
  * { box-sizing: border-box; margin: 0; padding: 0; }
  html, body { width: 1200px; height: 1200px; overflow: hidden; }
  body { background: var(--stage); position: relative; font-family: "Carlito", sans-serif; }

  .flyer {
    position: absolute; left: 40px; top: 204px;
    width: 1072px; height: 758px;
    transform: scale(1.0448); transform-origin: top left;
    background: var(--paper); overflow: hidden;
    box-shadow: 0 20px 40px rgba(0,0,0,.45);
  }
  .flyer-shapes { position: absolute; inset: 0; }
  .display { font-family: "Saira", sans-serif; }

  .headline {
    position: absolute; left: 56px; top: 48px;
    font-size: 56px; font-weight: 700; color: var(--sage); letter-spacing: .5px; line-height: 1;
  }
  .intro {
    position: absolute; left: 58px; top: 116px;
    font-size: 25px; font-weight: 600; color: var(--ink); line-height: 30px;
  }

  .brand {
    position: absolute; left: 760px; top: 62px;
    display: flex; align-items: center; gap: 16px;
    color: #2f8f86; font-family: "Saira", sans-serif; font-weight: 600;
  }
  .brand-dot { width: 70px; height: 70px; border-radius: 50%; background: #2f8f86; }
  .brand-name { font-size: 34px; line-height: 1; }
  .brand-type { font-size: 11px; letter-spacing: 4px; margin-top: 8px; text-transform: uppercase; }

  .hours {
    position: absolute; left: 64px; top: 252px;
    font-weight: 700; line-height: 1;
  }
  .hours-open { font-size: 66px; color: var(--sage); }
  .hours-days { font-size: 50px; color: var(--white); margin-top: -2px; }
  .hours-week { font-size: 50px; color: var(--orange); margin-top: -4px; }

  .social { position: absolute; left: 58px; top: 488px; list-style: none; }
  .social li {
    display: flex; align-items: center; gap: 12px;
    font-size: 23px; color: var(--ink); height: 28px;
  }
  .social-mark { width: 18px; height: 18px; background: #4a4a4a; border-radius: 3px; }

  .values {
    position: absolute; left: 298px; top: 530px; width: 200px;
    text-align: center; font-weight: 700; line-height: 1;
  }
  .values-warm { font-size: 40px; color: var(--ink); }
  .values-quirky { font-size: 40px; color: var(--orange); margin-top: -2px; }
  .values-approach { font-size: 19px; color: var(--ink); margin-top: 6px; font-weight: 600; }

  .contact-pill {
    position: absolute; left: 737px; top: 539px;
    width: 264px; height: 46px; border-radius: 23px;
    background: var(--white); color: var(--ink);
    display: flex; align-items: center; justify-content: center;
    font-size: 23px; font-weight: 600;
    box-shadow: 0 6px 8px rgba(0,0,0,.2);
  }
  .contact-lines {
    position: absolute; right: 80px; top: 614px;
    display: flex; color: var(--ink); font-size: 21px; line-height: 25px;
  }
  .contact-web { text-align: right; padding-right: 26px; border-right: 2px solid var(--ink); }
  .contact-phone { text-align: right; padding-left: 24px; }
  .address {
    position: absolute; right: 80px; top: 672px;
    font-size: 21px; color: var(--ink);
  }
</style>
</head>
<body>
<div class="flyer">
  <svg class="flyer-shapes" width="1072" height="758" viewBox="0 0 1072 758" xmlns="http://www.w3.org/2000/svg">
    <defs>
      <linearGradient id="paperGrad" x1="0" y1="0" x2="0" y2="1">
        <stop offset="0" stop-color="#f7f7f7"/><stop offset="1" stop-color="#e6e6e6"/>
      </linearGradient>
      <linearGradient id="clinicPhoto" x1="0" y1="0" x2="1" y2="1">
        <stop offset="0" stop-color="#eef2f3"/><stop offset=".55" stop-color="#dfe6e6"/><stop offset="1" stop-color="#c9b7a3"/>
      </linearGradient>
      <radialGradient id="portraitPhoto" cx=".55" cy=".55" r=".6">
        <stop offset="0" stop-color="#e6c596"/><stop offset=".6" stop-color="#f1ede6"/><stop offset="1" stop-color="#e8eef0"/>
      </radialGradient>
      <radialGradient id="badgeFill" cx=".5" cy=".35" r=".7">
        <stop offset="0" stop-color="#ffffff"/><stop offset="1" stop-color="#e4e4e4"/>
      </radialGradient>
    </defs>

    <rect class="paper" width="1072" height="758" fill="url(#paperGrad)"/>

    <!-- header swoosh -->
    <path d="M672 0 H1072 V222 H575 Q580 80 672 0 Z" fill="var(--charcoal)"/>
    <path d="M690 0 H1072 V214 H592 Q600 78 690 0 Z" fill="var(--sage)"/>
    <path d="M738 0 H1072 V214 H648 Q660 70 738 0 Z" fill="#f4f4f4"/>
    <rect x="575" y="214" width="497" height="10" fill="var(--charcoal)"/>

    <!-- hours band -->
    <rect x="0" y="224" width="620" height="6" fill="var(--sage)"/>
    <rect x="0" y="230" width="620" height="196" fill="var(--charcoal)"/>
    <rect x="0" y="426" width="620" height="6" fill="var(--sage)"/>

    <!-- clinic photo -->
    <rect x="650" y="226" width="422" height="276" fill="url(#clinicPhoto)" role="img" aria-label="Photo: vet with clipboard chatting with a pet owner holding a dachshund"/>

    <!-- contact band -->
    <path d="M0 718 C170 628 330 608 470 602 L640 500 H1072 V718 Z" fill="var(--charcoal)"/>
    <path d="M0 718 C180 640 330 622 470 616 L650 512 H1072 V718 Z" fill="var(--orange)"/>
    <rect x="0" y="718" width="1072" height="5" fill="var(--white)"/>
    <rect x="0" y="723" width="1072" height="35" fill="var(--sage)"/>

    <!-- portrait circle -->
    <circle cx="512" cy="395" r="194" fill="var(--white)"/>
    <circle cx="512" cy="395" r="186" fill="var(--sage)"/>
    <circle cx="512" cy="395" r="168" fill="url(#portraitPhoto)" role="img" aria-label="Photo: smiling vet with a golden labrador puppy"/>

    <!-- values badge -->
    <circle cx="398" cy="587" r="118" fill="var(--white)"/>
    <circle cx="398" cy="587" r="112" fill="var(--sky)"/>
    <circle cx="398" cy="587" r="101" fill="url(#badgeFill)"/>
  </svg>

  <h1 class="headline display">DID YOU KNOW?</h1>
  <p class="intro display">Coral Bay now has its own<br>Veterinary Clinic</p>

  <div class="brand">
    <span class="brand-dot"></span>
    <div>
      <div class="brand-name">Kindred Paws</div>
      <div class="brand-type">Veterinary Clinic</div>
    </div>
  </div>

  <div class="hours display">
    <div class="hours-open">OPEN</div>
    <div class="hours-days">7 DAYS</div>
    <div class="hours-week">A WEEK</div>
  </div>

  <ul class="social">
    <li><span class="social-mark"></span>@KindredPawsCoral</li>
    <li><span class="social-mark"></span>@kindredpawsvet</li>
    <li><span class="social-mark"></span>@kindredpawsclinic</li>
  </ul>

  <div class="values display">
    <div class="values-warm">Warm</div>
    <div class="values-quirky">quirky</div>
    <div class="values-approach">Approachable</div>
  </div>

  <div class="contact-pill display">How To Contact Us?</div>
  <div class="contact-lines">
    <div class="contact-web">www.kindredpaws.example<br>hello@kindredpaws.example</div>
    <div class="contact-phone">Call: 800-555-0142<br>Call: 04 555 0199</div>
  </div>
  <p class="address">Silver Brook Arcade, Building 4, Mezzanine level</p>
</div>
</body>
</html>
```